New Website

New website is to be the same as Copper Lantern.

Website needs to be fully functional, with only text and logo to be added by client at a later date.

Logo has been added for reference.

Reason: waiting for the final submissions to be completed.

```html
<!DOCTYPE html>
<html lang="en">
<head>
<meta charset="utf-8">
<title>Verdant – Register</title>
<link href="https://fonts.googleapis.com/css2?family=Roboto:ital,wght@0,300;0,400;0,500;0,700;1,400&display=swap" rel="stylesheet">
<style>
:root{
  --navy:#1d3f8f;
  --navy-deep:#183478;
  --teal:#2a8fae;
  --sky:#5ec8e5;
  --ink:#2b2b2b;
  --grey-bg:#efefef;
  --white:#ffffff;
  --btn-dark:#3a3a3a;
  --link:#ffffff;
  --shade:rgba(0,0,0,0.56);
}
*{margin:0;padding:0;box-sizing:border-box}
html,body{width:853px;height:1200px;overflow:hidden}
body{font-family:'Roboto',sans-serif;color:var(--ink);background:var(--grey-bg);position:relative}
.abs{position:absolute}
/* header */
.site-header{left:0;top:0;width:853px;height:43px;background:var(--white)}
.brand{left:134px;top:10px;display:flex;align-items:center;gap:8px}
.brand-mark{width:44px;height:44px;border-radius:50%;background:var(--navy)}
.brand-name{font-size:24px;font-weight:400;color:var(--navy);letter-spacing:1px;line-height:1}
.brand-tag{left:187px;top:46px;font-size:6px;color:var(--navy)}
.main-nav{left:332px;top:26px;display:flex;gap:15px;font-size:10px;color:#333}
.btn-small{height:17px;font-size:8px;color:var(--white);background:var(--navy);display:flex;align-items:center;justify-content:center}
.sign-in{left:595px;top:19px;width:52px}
.or{left:653px;top:23px;font-size:8px;color:#555}
.register-top{left:671px;top:19px;width:52px}
.sub-bar{left:0;top:43px;width:853px;height:29px;background:var(--navy)}
.make-expert{left:465px;top:43px;width:125px;height:29px;background:var(--navy-deep);color:var(--white);font-size:11px;display:flex;align-items:center;justify-content:center;gap:6px}
.find-expert{left:596px;top:43px;width:127px;height:34px;background:var(--teal);color:var(--white);font-size:11px;display:flex;align-items:center;justify-content:center;gap:6px}
/* hero */
.hero{left:0;top:72px;width:853px;height:275px;background:#f1f1f1}
.hero-photo{left:560px;top:72px;width:293px;height:238px;background:linear-gradient(120deg,#e9e9e9,#bfc4c8 60%,#9aa0a6)}
.hero-title{left:144px;top:136px;font-size:21px;line-height:26px;font-weight:400}
.hero-sub{left:144px;top:212px;font-size:14px}
.hero-btn{left:144px;top:254px;width:122px;height:17px;background:var(--navy);color:var(--white);font-size:8px;display:flex;align-items:center;justify-content:center}
.dots{left:198px;top:309px;display:flex;gap:3px}
.dots span{width:5px;height:5px;border-radius:50%;background:#444}
/* testimonial */
.testimonial{left:0;top:347px;width:853px;height:199px;background:var(--navy-deep);color:#c9d3ea;text-align:center}
.testimonial h2{position:absolute;left:0;width:853px;top:43px;font-size:17px;font-weight:400;color:#e6ecf7}
.testimonial blockquote{position:absolute;left:212px;width:429px;top:82px;font-size:8.5px;line-height:13.5px;font-style:italic}
.testimonial .who{position:absolute;left:0;width:853px;top:146px;font-size:11px;color:#e6ecf7}
.testimonial .role{position:absolute;left:0;width:853px;top:162px;font-size:6.5px}
.arrow{top:84px}
/* video */
.video-title{left:0;width:853px;top:568px;text-align:center;font-size:21px}
.video-frame{left:207px;top:616px;width:439px;height:196px;background:linear-gradient(180deg,#d8d3cc,#bfb7ad 55%,#e6e4e1)}
.play{left:406px;top:702px;width:40px;height:25px;background:rgba(0,0,0,0.6);border-radius:3px}
/* experts */
.experts-title{left:0;width:853px;top:844px;text-align:center;font-size:17px}
.expert{top:896px;width:140px}
.expert .photo{width:94px;height:94px;background:linear-gradient(160deg,#e4e4e4,#b9b3ad);border:2px solid #fff}
.expert .name{margin-top:19px;font-size:12px;font-weight:500;color:var(--navy)}
.expert .meta{font-size:8.5px;line-height:11px;color:#333}
.band{left:0;top:1060px;width:853px;height:125px;background:#e6e6e6}
.band p{position:absolute;left:170px;width:513px;top:25px;text-align:center;font-size:11.5px;line-height:14.5px;font-weight:300}
.see-all{left:385px;top:1148px;width:83px;height:17px;background:var(--navy);color:var(--white);font-size:7.5px;display:flex;align-items:center;justify-content:center}
.footer{left:0;top:1185px;width:853px;height:15px;background:#2b2b2b}
/* modal */
.shade{left:0;top:0;width:853px;height:1200px;background:var(--shade)}
.modal{left:266px;top:72px;width:321px;height:275px;background:var(--sky);color:#1e2a33}
.modal h1{position:absolute;left:0;width:321px;top:14px;text-align:center;color:var(--white);font-size:21px;font-weight:400}
.field{position:absolute;width:143px;height:32px;background:var(--white);border:1px solid #cfd8dc;font-size:10px;color:#777;padding:0 9px;display:flex;align-items:center}
.optin{position:absolute;left:16px;top:133px;font-size:10px;display:flex;align-items:center;gap:12px}
.box{width:8px;height:8px;background:#fff;border:1px solid #888}
.terms{position:absolute;left:0;width:321px;top:157px;text-align:center;font-size:10px;line-height:14.5px}
.terms a{color:var(--link);text-decoration:none}
.modal-btn{position:absolute;left:96px;top:205px;width:129px;height:17px;background:var(--btn-dark);color:var(--white);font-size:8px;display:flex;align-items:center;justify-content:center}
.already{position:absolute;left:0;width:321px;top:242px;text-align:center;font-size:10px}
.already a{color:var(--link);text-decoration:none}
</style>
</head>
<body>
<header class="site-header abs"></header>
<div class="brand abs"><span class="brand-mark"></span><span class="brand-name">VERDANT</span></div>
<div class="brand-tag abs">partners for lasting growth</div>
<nav class="main-nav abs"><span>How it Works</span><span>Products</span><span>Blog</span><span>Help</span></nav>
<div class="btn-small sign-in abs">Sign In</div>
<div class="or abs">OR</div>
<div class="btn-small register-top abs">Register</div>
<div class="sub-bar abs"></div>
<div class="make-expert abs"><svg width="7" height="5"><path d="M0 0h7L3.5 5z" fill="#fff"/></svg>Make Me An Expert</div>
<div class="find-expert abs"><svg width="11" height="11"><circle cx="4.5" cy="4.5" r="3.5" stroke="#fff" stroke-width="1.5" fill="none"/><path d="M7 7l3 3" stroke="#fff" stroke-width="1.5"/></svg>Find Your Expert</div>

<section class="hero abs"></section>
<div class="hero-photo abs" role="img" aria-label="Consultant working at a desk in a bright office"></div>
<div class="hero-title abs">The Right Expert.<br>Right Now™</div>
<div class="hero-sub abs">Consulting Made Simple</div>
<div class="hero-btn abs">Browse Business Categories</div>
<div class="dots abs"><span></span><span></span><span></span></div>

<section class="testimonial abs">
  <h2>What Clients Are Saying</h2>
  <blockquote>I felt this session was on target and the solutions we discussed are real candidates. We are only one discussion away from recommending a winning plan. Owen Hale was articulate, knowledgeable, experienced, and concise. Very helpful!</blockquote>
  <div class="who">Mara Ellison</div>
  <div class="role">—CEO, the circuit works</div>
  <svg class="arrow abs" style="left:146px" width="12" height="22"><path d="M10 1L2 11l8 10" stroke="#c9d3ea" stroke-width="1.5" fill="none"/></svg>
  <svg class="arrow abs" style="left:697px" width="12" height="22"><path d="M2 1l8 10-8 10" stroke="#c9d3ea" stroke-width="1.5" fill="none"/></svg>
</section>

<h2 class="video-title abs" style="font-weight:400">Watch The Video</h2>
<div class="video-frame abs" role="img" aria-label="Team of consultants reviewing documents around a table"></div>
<svg class="play abs" viewBox="0 0 40 25"><rect width="40" height="25" rx="3" fill="rgba(0,0,0,0.55)"/><path d="M16 7l9 5.5-9 5.5z" fill="#fff"/></svg>

<h2 class="experts-title abs" style="font-weight:400">Introducing Your Business Expert Network</h2>
<div class="expert abs" style="left:163px"><div class="photo" role="img" aria-label="Portrait of expert Dana Wexford"></div><div class="name">Dana Wexford</div><div class="meta">CEO • Northfield Group, Inc.<br>Cloudline Services</div></div>
<div class="expert abs" style="left:307px"><div class="photo" role="img" aria-label="Portrait of expert Rita Calder"></div><div class="name">Rita Calder</div><div class="meta">Senior Director<br>Market Research</div></div>
<div class="expert abs" style="left:452px"><div class="photo" role="img" aria-label="Portrait of expert Ronald Ashcombe"></div><div class="name">Ronald Ashcombe</div><div class="meta">Principal<br>Strategic Messaging</div></div>
<div class="expert abs" style="left:597px"><div class="photo" role="img" aria-label="Portrait of expert Jenna Marlow"></div><div class="name">Jenna Marlow</div><div class="meta">Chief Operating Officer<br>Manufacturing Strategy</div></div>

<section class="band abs"><p>All of our experts meet high qualification requirements and undergo rigorous testing for their specific skills and consulting abilities. Learn more about how experts are chosen. If you think you have what it takes, become an expert today.</p></section>
<div class="see-all abs">See All Experts ›</div>
<footer class="footer abs"></footer>

<div class="shade abs"></div>
<section class="modal abs" aria-label="Register for Free">
  <h1>Register for Free</h1>
  <div class="field" style="left:15px;top:57px">First Name</div>
  <div class="field" style="left:162px;top:57px">Last Name</div>
  <div class="field" style="left:15px;top:93px">Email Address</div>
  <div class="field" style="left:162px;top:93px">Re-Enter Email</div>
  <div class="optin"><svg class="box" viewBox="0 0 8 8" style="border:none"><rect x=".5" y=".5" width="7" height="7" fill="#fff" stroke="#888"/><path d="M2 4l1.5 1.5L6 2.5" stroke="#333" fill="none"/></svg>Keep me in the loop on new experts and Verdant news.</div>
  <p class="terms">By clicking on <a>"Register"</a> you confirm you accept the<br><a>Terms of Use</a> and the <a>Privacy Policy.</a></p>
  <div class="modal-btn">Register</div>
  <p class="already">Already registered? <a>Sign in</a></p>
</section>
</body>
</html>
```